Business Card Design Project for an authorized Hanabo Dealer in Jakarta, Indonesia

Looking to revitalize both of our company's logo and the business card design. The business card has to have our company's logo and the Hanabo "way of life" logo. Te final design has to have professional and bold look.

For more info on our logo and Hanabo:
Www.rimbakarsa.co.id

```html
<!DOCTYPE html>
<html lang="en">
<head>
<meta charset="utf-8">
<title>Rimba Karsa Business Card</title>
<link href="https://fonts.googleapis.com/css2?family=Source+Sans+3:wght@400;600;700&display=swap" rel="stylesheet">
<style>
  :root {
    --navy: #2c2a6f;
    --red: #e3212b;
    --ink: #2a2a2a;
    --stage: #e6e4e1;
    --card-top: #ffffff;
    --card-bottom: #dcdcde;
    --rule: #c9c9cf;
  }
  html, body {
    margin: 0;
    padding: 0;
    width: 1200px;
    height: 900px;
    overflow: hidden;
    background: var(--stage);
    font-family: "Source Sans 3", sans-serif;
  }
  .stage { position: relative; width: 1200px; height: 900px; }
  .card {
    position: absolute;
    top: 290px;
    width: 528px;
    height: 321px;
    overflow: hidden;
    background: linear-gradient(180deg, var(--card-top) 0%, #f3f3f4 45%, var(--card-bottom) 100%);
    box-shadow: 0 4px 14px rgba(0,0,0,0.18);
  }
  .card--front { left: 57px; }
  .card--back {
    left: 616px;
    background: radial-gradient(ellipse at 50% 42%, #ffffff 0%, #f2f2f3 55%, #dfdfe1 100%);
  }

  .brand {
    position: absolute;
    color: var(--navy);
    font-weight: 700;
    line-height: 1;
    white-space: nowrap;
  }
  .card--front .brand { left: 45px; top: 44px; font-size: 40px; letter-spacing: 0.5px; }
  .card--back .brand { left: 0; right: 0; top: 110px; text-align: center; font-size: 62px; letter-spacing: 1px; }

  .partner {
    position: absolute;
    left: 360px;
    top: 38px;
    display: flex;
    align-items: center;
    gap: 8px;
  }
  .partner__name { color: var(--red); font-weight: 700; font-size: 15px; letter-spacing: 0.5px; }
  .partner__badge { width: 54px; height: 54px; background: #1d2a3a; }

  .person { position: absolute; left: 24px; width: 190px; top: 180px; text-align: center; }
  .person__name { color: var(--navy); font-weight: 600; font-size: 19px; margin: 0; }
  .person__role { color: var(--ink); font-size: 11px; margin: 1px 0 0; }
  .person__phone { color: var(--ink); font-size: 11px; margin: 10px 0 0; }

  .divider {
    position: absolute;
    left: 216px;
    top: 166px;
    width: 1px;
    height: 64px;
    background: linear-gradient(180deg, transparent, var(--rule), transparent);
  }

  .company { position: absolute; left: 243px; top: 146px; color: var(--ink); font-size: 12.5px; line-height: 17.5px; }
  .company__name { color: var(--navy); font-weight: 700; margin: 0; }
  .company__line { font-weight: 700; margin: 0; }
  .company__contact { margin: 17px 0 0; padding: 0; list-style: none; }

  .band { position: absolute; left: 0; bottom: 0; width: 528px; height: 19px; }

  .rule {
    position: absolute;
    left: 105px;
    top: 201px;
    width: 318px;
    height: 2px;
    background: linear-gradient(90deg, transparent, var(--navy), transparent);
  }
  .tagline { position: absolute; left: 0; right: 0; top: 216px; text-align: center; margin: 0; color: var(--navy); font-weight: 700; font-size: 13px; }
  .website { position: absolute; left: 0; right: 0; top: 294px; text-align: center; margin: 0; color: var(--navy); font-size: 12px; }
</style>
</head>
<body>
<main class="stage">
  <section class="card card--front" aria-label="Business card front">
    <div class="brand">Rimba Karsa</div>
    <div class="partner">
      <span class="partner__name">Hanabo</span>
      <span class="partner__badge"></span>
    </div>

    <div class="person">
      <p class="person__name">Dimas Wicaksono</p>
      <p class="person__role">Managing Director</p>
      <p class="person__phone">HP : 0812 4470 2918</p>
    </div>

    <div class="divider"></div>

    <div class="company">
      <p class="company__name">PT. Rimba Karsa Abadi</p>
      <p class="company__line">Authorized Hanabo Dealer</p>
      <p class="company__line">Sales, Service, Spare Parts.</p>
      <ul class="company__contact">
        <li>Jl. Raya Cempaka Km.5, Depok, Jawa Barat, 16412</li>
        <li>Telp : (021) 7762 310, 7762 311</li>
        <li>Fax &nbsp;: (021) 7762 319</li>
        <li>Email : dimas_w@rimbakarsa.co.id</li>
      </ul>
    </div>

    <svg class="band" viewBox="0 0 528 19" preserveAspectRatio="none" aria-hidden="true">
      <rect x="0" y="0" width="528" height="19" fill="var(--navy)"/>
      <polygon points="466,19 490,0 528,0 528,19" fill="var(--red)"/>
      <polygon points="454,19 478,0 484,0 460,19" fill="#ffffff"/>
    </svg>
  </section>

  <section class="card card--back" aria-label="Business card back">
    <div class="brand">Rimba Karsa</div>
    <div class="rule"></div>
    <p class="tagline">Authorized Hanabo Dealer Sales, Service, Spare Parts.</p>
    <p class="website">www.rimbakarsa.co.id</p>
  </section>
</main>
</body>
</html>
```